mooncake box cover sleeve

This is a mooncake packaging box design project.
2 sizes box: 4 pcs & 6 pcs (as shown in the mock-up picture).
The length of the box is the same: 20 cm.
Dimensions, please see pictures 1 & 2.
prefer sleeve area/dimension: 20cm x 15cm
(15cm width is good to use on both boxes, IMPORTANT. please follow this scale in your design & mock up)
Product Name: Hong Kong Style Custard Mooncake with Flaky Egg Waffle Crust. 雞蛋仔酥皮奶黃月
Product Information:
Handmade Custard Mooncake.
For the Moon Festival. Once a year, to celebrate the biggest and brightest moon of the year.
Mooncakes are expensive products. For friends & family, and many businesses for their VIP customers.
Our mooncake is made with all-natural ingredients, authentic Hong Kong-style custard, using a traditional grandfather recipe, and baked with a Hong Kong-style egg waffle crust (this crust is the key and unique selling point).
Key points / must-have / need to be emphasized in this design.
- Traditional Hong Kong-style Custard
- Baked with HK-style Egg Waffle crust
- All-natural ingredients
- Luxury, high-end feel
- A full, bright moon.
- Yellow Custard
- Made in USA
- Add a line for the product name in Chinese 雞蛋仔酥皮奶黃月
I need 1 paper sleeve design that works for both boxes.
I found a company with the same concept for your reference.
See pictures 3 & 4.
**IMPORTANT** 1 sleeve works for both boxes.
Color of the box:
Open. I will order plain color. You can pick the best color to match your design.
The 4 pcs & 6 pcs can be different colors.
Preferred colors: Yellow, Black, Orange, Red tone.
NO on: Blue, purple, green, white.
Color theme of the sleeve design:
Yellow, Golden, Orange, Dark luxury, healthy earth tone, to match my logo.
This is a custard mooncake product, luxury, fine bakery products. Please give a feeling of: organic, clean, earth tone, healthy, fresh feeling.
(OK to use a little bit of green/earth tone, just to avoid Green on the plain box color)
Useful element for MoonFestival:
- Full moon
- Lantern
- Mooncake
- Family gathering
Please feel free to use all the add-on printing features to add a high-end feel. *GOLD STAMP FOIL is a must, the more the better*
Spot UV, embossed, are all welcome.
Home-Baked instructions:
We used to have a separate card, printed both sides (attached).
I would like to print this on BOTH inside the open box (see pic 2), and on the back of the sleeve. So no more cards needs to be giving out.
Please feel free to re-design a bit. thanks.
Information must have:
Front panel:
- Product Name
- Company Logo
- Egg Waffle image
- Made in California, USA (with the flag)
Back panel:
- Nutrition Fact
- Save spaces for ingredients listing (will provide later)
- Home-Baked instructions (Follow attached square card for info, make is shorter and simpler, Make it persuasive to try, give an easy feeling, Highly recommend the customer to follow)
- Fresh Baked On (A spaces for Date Stamp 2x5cm)
For details, please visit our website:
www.tovamistbakes.com
The boxes you see there are 2025.
We want a complete face lift in 2026. Thank you.
****New Message Jan 09, 2026*****
Dear all designers,
- No stock picture purchase please.
- uploaded new files for reference: please use "Lion Rock" (this one I own it, bought from previous project)
- 4 Icons must clearly shown on Front Panel.
- Space for Date Stamp.
Because this product has no preservatives, it is important to enjoy it before the date.
Please use my handwriting as a reference. Please forgive me. My drawing is not good, and please implement it with your professional skills. Without a face-to-face meeting, this is the best I can do to explain. Thanks again, all.

```html
<!DOCTYPE html>
<html lang="en">
<head>
<meta charset="utf-8">
<title>Mooncake Sleeve – Back Panel</title>
<link href="https://fonts.googleapis.com/css2?family=Playfair+Display:wght@700;800&family=Libre+Franklin:wght@400;700;800&display=swap" rel="stylesheet">
<style>
  :root {
    --backdrop: #f1d6c6;
    --sleeve-green: #1f532e;
    --foil-gold: #dcc57c;
    --foil-gold-soft: #c9b06a;
    --art-tone: rgba(220,197,124,.38);
  }
  * { box-sizing: border-box; margin: 0; padding: 0; }
  html, body { width: 1200px; height: 1200px; overflow: hidden; }
  body { background: var(--backdrop); position: relative; }

  .sleeve-back {
    position: absolute; left: 358px; top: 50px;
    width: 484px; height: 1100px;
    background: var(--sleeve-green);
    color: var(--foil-gold);
    font-family: "Playfair Display", Georgia, serif;
    font-variant-numeric: lining-nums;
    overflow: hidden;
  }
  .art { position: absolute; background: var(--art-tone); }
  .art--hen { left: 12px; top: 58px; width: 96px; height: 76px; border-radius: 45% 45% 30% 30%; }
  .art--cranes { left: 332px; top: 28px; width: 128px; height: 54px; border-radius: 40%; }
  .art--crane-lone { left: 392px; top: 742px; width: 62px; height: 40px; border-radius: 40%; }
  .art--ox-cart { left: 226px; top: 862px; width: 258px; height: 238px; border-radius: 46% 30% 0 38%; }

  .guide-heading {
    position: absolute; top: 183px; left: 0; width: 100%;
    text-align: center; font-size: 25px; font-weight: 700; line-height: 35px;
  }
  .step-title { position: absolute; font-size: 21px; font-weight: 700; }
  .step-body { position: absolute; font-size: 11.5px; font-weight: 700; line-height: 17px; }
  .step-1 .step-title { left: 39px; top: 320px; }
  .step-1 .step-body { left: 39px; top: 350px; width: 210px; }
  .step-2 .step-title { left: 233px; top: 440px; }
  .step-2 .step-body { left: 233px; top: 478px; width: 220px; }

  .icon { position: absolute; stroke: var(--foil-gold); fill: none; stroke-width: 2.5; stroke-linecap: round; stroke-linejoin: round; }
  .icon--snow { left: 278px; top: 305px; width: 118px; height: 118px; }
  .icon--fryer { left: 74px; top: 462px; width: 90px; height: 126px; }

  .nutrition {
    position: absolute; left: 34px; top: 660px; width: 218px;
    font-family: "Libre Franklin", Arial, sans-serif; color: var(--foil-gold);
  }
  .nutrition h2 { font-size: 27px; font-weight: 800; letter-spacing: -.3px; line-height: 30px; }
  .nutrition .servings { font-size: 8px; line-height: 10px; border-bottom: 6px solid var(--foil-gold); padding-bottom: 3px; }
  .nutrition .servings strong { display: flex; justify-content: space-between; }
  .nutrition .calories {
    display: grid; grid-template-columns: 82px 68px 68px; align-items: end;
    border-bottom: 4px solid var(--foil-gold); padding: 2px 0;
  }
  .nutrition .calories .label { font-size: 12px; font-weight: 800; }
  .nutrition .calories .num { font-size: 18px; font-weight: 800; text-align: right; padding-right: 4px; }
  .nutrition .calories .num small { display: block; font-size: 6px; font-weight: 400; text-align: center; }
  .nutrition table { width: 100%; border-collapse: collapse; font-size: 6.4px; line-height: 8.4px; }
  .nutrition td { border-bottom: .6px solid var(--foil-gold-soft); padding: 0 1px; white-space: nowrap; }
  .nutrition td.sub { padding-left: 7px; }
  .nutrition td.sub2 { padding-left: 14px; }
  .nutrition td.v { width: 22px; }
  .nutrition td.p { text-align: right; width: 18px; padding-right: 4px; }
  .nutrition tr.dv td { font-size: 5.5px; text-align: right; }
  .nutrition tr.thick td { border-bottom: 3px solid var(--foil-gold); }
  .nutrition .footnote { font-size: 5px; line-height: 6.5px; margin-top: 3px; }

  .fresh-baked {
    position: absolute; left: 36px; top: 1019px;
    font-size: 21px; font-weight: 700;
  }
</style>
</head>
<body>
  <section class="sleeve-back">
    <div class="art art--hen" role="img" aria-label="Engraved gold illustration of a hen"></div>
    <div class="art art--cranes" role="img" aria-label="Engraved gold illustration of two flying cranes"></div>

    <p class="guide-heading">It’s a step-by-step preparation<br>guide for frozen mooncakes,<br>using an air fryer.</p>

    <div class="step-1">
      <h3 class="step-title">Step 1&nbsp; Freeze It</h3>
      <p class="step-body">Once you receive your package,<br>store it in the freezer<br>Do not open the plastic wraps</p>
    </div>

    <svg class="icon icon--snow" viewBox="0 0 120 120" aria-hidden="true">
      <g transform="translate(60 60)">
        <g id="arm">
          <line x1="0" y1="-8" x2="0" y2="-54"/>
          <polyline points="-10,-30 0,-20 10,-30"/>
          <polyline points="-9,-44 0,-35 9,-44"/>
          <circle cx="0" cy="-14" r="1.6"/>
        </g>
        <use href="#arm" transform="rotate(45)"/>
        <use href="#arm" transform="rotate(90)"/>
        <use href="#arm" transform="rotate(135)"/>
        <use href="#arm" transform="rotate(180)"/>
        <use href="#arm" transform="rotate(225)"/>
        <use href="#arm" transform="rotate(270)"/>
        <use href="#arm" transform="rotate(315)"/>
      </g>
    </svg>

    <svg class="icon icon--fryer" viewBox="0 0 90 126" aria-hidden="true">
      <rect x="4" y="4" width="82" height="118" rx="10"/>
      <rect x="16" y="14" width="58" height="24" rx="5"/>
      <circle cx="28" cy="26" r="3"/>
      <circle cx="45" cy="26" r="3"/>
      <circle cx="62" cy="26" r="3"/>
      <line x1="4" y1="50" x2="86" y2="50"/>
      <rect x="16" y="62" width="58" height="48" rx="6"/>
      <path d="M38 62 v24 a7 7 0 0 0 14 0 v-24"/>
    </svg>

    <div class="step-2">
      <h3 class="step-title">Step 2 Air Fry It</h3>
      <p class="step-body">Remove all plastic wraps and trays<br>Place the frozen mooncakes into<br>the air fryer<br>Air fry at 360°F for 8 minutes<br>Let it sit for 1 minute before<br>serving<br>Caution: Product may be hot</p>
    </div>

    <div class="nutrition">
      <h2>Nutrition Facts</h2>
      <div class="servings">
        Each sachet contains 1 mooncake · 2 servings
        <strong><span>Serving size</span><span>1/2 mooncake (32g)</span></strong>
      </div>
      <div class="calories">
        <span class="label">Calories</span>
        <span class="num"><small>per serving</small>120</span>
        <span class="num"><small>per mooncake</small>240</span>
      </div>
      <table>
        <tr class="dv"><td></td><td colspan="2">% Daily Value*</td><td colspan="2">% Daily Value*</td></tr>
        <tr><td>Total Fat</td><td class="v">6g</td><td class="p">8%</td><td class="v">12g</td><td class="p">15%</td></tr>
        <tr><td class="sub">Saturated Fat</td><td class="v">4g</td><td class="p">20%</td><td class="v">8g</td><td class="p">40%</td></tr>
        <tr><td class="sub">Trans Fat</td><td class="v">0g</td><td class="p"></td><td class="v">0g</td><td class="p"></td></tr>
        <tr><td>Cholesterol</td><td class="v">25mg</td><td class="p">8%</td><td class="v">50mg</td><td class="p">16%</td></tr>
        <tr><td>Sodium</td><td class="v">30mg</td><td class="p">1%</td><td class="v">60mg</td><td class="p">3%</td></tr>
        <tr><td>Total Carbohydrate</td><td class="v">14g</td><td class="p">5%</td><td class="v">27g</td><td class="p">10%</td></tr>
        <tr><td class="sub">Dietary Fiber</td><td class="v">0g</td><td class="p">0%</td><td class="v">1g</td><td class="p">4%</td></tr>
        <tr><td class="sub">Total Sugars</td><td class="v">6g</td><td class="p"></td><td class="v">12g</td><td class="p"></td></tr>
        <tr><td class="sub2">Includes Added Sugars</td><td class="v">5g</td><td class="p">10%</td><td class="v">11g</td><td class="p">22%</td></tr>
        <tr class="thick"><td>Protein</td><td class="v">2g</td><td class="p"></td><td class="v">4g</td><td class="p"></td></tr>
        <tr><td>Vitamin D</td><td class="v">0mcg</td><td class="p">0%</td><td class="v">0mcg</td><td class="p">0%</td></tr>
        <tr><td>Calcium</td><td class="v">21mg</td><td class="p">2%</td><td class="v">42mg</td><td class="p">4%</td></tr>
        <tr><td>Iron</td><td class="v">1mg</td><td class="p">4%</td><td class="v">1mg</td><td class="p">6%</td></tr>
        <tr><td>Potassium</td><td class="v">40mg</td><td class="p">0%</td><td class="v">80mg</td><td class="p">2%</td></tr>
      </table>
      <p class="footnote">*The % Daily Value tells you how much a nutrient in a serving of food contributes to a daily diet. 2,000 calories a day is used for general nutrition advice.</p>
    </div>

    <div class="art art--crane-lone" role="img" aria-label="Engraved gold illustration of a flying crane"></div>
    <div class="art art--ox-cart" role="img" aria-label="Engraved gold illustration of an ox pulling a pagoda-roofed carriage"></div>

    <p class="fresh-baked">Fresh Baked On</p>
  </section>
</body>
</html>
```